SEO marketing site

I need a design only for an SEO/Marketing project I have in mind. I have bought the domain Brovelle.example and want to aim this project at businesses who want to push their business further. WHEN I SAY DESIGN ONLY, I MEAN NO PROGRAMMING. HOWEVER, I DO NEED THE DESIGNER TO PUT THIS SITE ONLINE. $300 IS A LOT OF MONEY FOR A TEMPLATE YOU CAN PURCHASE FOR $60 WITH SOME CUSTOMISATION.

The idea is that businesses will register with us and will be offered two different kinds of services. They can make use of our scripts to check their back links, rankings, compare with competitors and a number of other marketing tools. The other service we provide is that we offer them an SEO service at a very competitive price. We will handle social networking, link building, article submission, directory submission, social bookmarking etc etc at a reasonable monthly fee.

I quorix tiled look/flat design is what I really like, and I want to give off a professional vibe. This is the kind of site I wish to go for.

JUST TO REPEAT, I NEED A DESIGN TO BE PUT ONLINE, I.E PSD TO HTML CONVERSION. MY PROGRAMMERS WILL CODE THE CLIENT AREA THEMSELVES.

Target Market(s)

Other businesses

Industry/Entity Type

Marketing

Requirements
Must have
• Quorix 5 or flat design look. Even a site, similar to plumtower, is quite attractive. I would like a killer design for the site.

```html
<!DOCTYPE html>
<html lang="en">
<head>
<meta charset="utf-8">
<title>Brovelle – SEO Tools</title>
<link href="https://fonts.googleapis.com/css2?family=Arimo:wght@400;700&display=swap" rel="stylesheet">
<style>
:root{
  --ink:#1d2b30;
  --deep:#1d4a53;
  --deeper:#163b43;
  --accent:#3fb3cc;
  --accent-soft:#b9e2ec;
  --line:#a6d6e2;
  --muted:#5b6b70;
  --rule:#e1e6e8;
  --white:#ffffff;
  --orange:#f0622a;
  --green:#58b83b;
  --blue:#1c8fd6;
  --yellow:#f3d21b;
}
*{box-sizing:border-box;margin:0;padding:0}
html,body{width:1200px;height:3602px;overflow:hidden}
body{font-family:"Arimo",Arial,sans-serif;color:var(--ink);background:var(--white);position:relative}
.abs{position:absolute}
.rule{position:absolute;left:110px;width:980px;height:2px;background:var(--rule)}

/* header */
.site-header{position:absolute;top:0;left:0;width:1200px;height:62px;background:var(--deep)}
.brand{position:absolute;left:110px;top:12px;color:var(--white);font-size:34px;letter-spacing:1px}
.nav{position:absolute;left:512px;top:0;display:flex;height:62px;align-items:center;gap:18px;font-size:14px;color:var(--white);white-space:nowrap}
.nav .current{border-bottom:3px solid var(--white);padding:21px 4px 17px}
.btn-signup-sm{position:absolute;left:972px;top:20px;width:64px;height:26px;background:var(--accent-soft);color:var(--deep);font-size:14px;text-align:center;line-height:26px;border-radius:3px}
.lang{position:absolute;left:1048px;top:22px;width:42px;height:22px;background:var(--white);border-radius:3px}
.lang i{position:absolute;left:6px;top:6px;width:16px;height:10px;background:#d33}

/* hero */
.hero{position:absolute;top:62px;left:0;width:1200px;height:673px;background:linear-gradient(180deg,#9fdcee 0%,#c9eef7 45%,#e9f8fb 70%,#fdfdf5 100%)}
.hero-clouds{position:absolute;left:0;top:420px;width:1200px;height:253px;background:linear-gradient(180deg,rgba(255,255,255,0) 0%,#ffffff 45%,#fbfbf1 100%)}
.hero-title{position:absolute;top:62px;left:0;width:1200px;text-align:center;font-size:50px;font-weight:700;color:var(--white);text-shadow:0 2px 6px rgba(40,110,130,.35)}
.feature{position:absolute;top:160px;width:300px;text-align:center}
.feature svg{display:block;margin:0 auto}
.feature span{display:block;margin-top:12px;font-size:23px;color:var(--ink)}
.btn-dark{background:var(--deep);color:var(--white);text-align:center;border-radius:3px}
.hero-cta{position:absolute;left:553px;top:328px;width:124px;height:40px;line-height:40px;font-size:22px}
.hero-note{position:absolute;top:384px;left:0;width:1200px;text-align:center;font-size:13px}

/* intro */
.intro{position:absolute;top:680px;left:0;width:1200px;text-align:center}
.intro h1{font-size:52px;font-weight:400;color:var(--ink)}
.intro .lead{font-size:17px;margin-top:4px}
.intro .accent{font-size:27px;color:var(--accent);margin-top:2px}
.intro .small{font-size:13px;margin-top:0}

/* stats */
.stats-title{position:absolute;left:110px;top:904px;font-size:38px}
.stats-sub{position:absolute;left:110px;top:950px;width:470px;font-size:19px;color:var(--accent);line-height:22px}
.visit-bar{position:absolute;left:110px;top:1016px;width:460px;height:42px;background:var(--accent-soft);font-size:23px;font-weight:700;line-height:42px;padding-left:16px}
.legend{position:absolute;left:306px;top:1073px;font-size:20px}
.legend li{list-style:none;position:relative;padding-left:20px;margin-bottom:17px;line-height:22px}
.legend li small{display:block;font-size:14px}
.legend li i{position:absolute;left:0;top:5px;width:12px;height:12px}
.dashboard-shot{position:absolute;left:600px;top:906px;width:490px;height:420px;background:linear-gradient(180deg,#2a2a2a 0%,#3b3b3b 60%,#d8d8d8 85%,#eeeeee 100%);border-radius:8px}

/* clients */
.section-title{position:absolute;left:0;width:1200px;text-align:center;font-size:32px}
.clients{position:absolute;left:135px;top:1500px;width:930px;height:40px;display:flex;justify-content:space-between;align-items:center;color:#9aa3a6;font-size:24px}

/* chart */
.chart-icon{position:absolute;left:555px;top:1680px;width:64px;height:54px}
.chart-title{position:absolute;left:629px;top:1672px;font-size:26px}
.chart-text{position:absolute;left:629px;top:1710px;width:460px;font-size:14px;line-height:19px;color:var(--ink)}
.tooltip{position:absolute;left:502px;top:1812px;width:216px;height:74px;background:#6f8a8d;color:var(--white);font-size:13px;line-height:17px;padding:12px 8px}

/* columns */
.col{position:absolute;top:2250px;width:300px;text-align:center}
.col h3{font-size:22px;font-weight:400}
.col .art{width:140px;height:110px;margin:22px auto 0;border-radius:6px}
.col p{font-size:14px;line-height:18px;margin-top:16px}
.col .btn-dark{display:inline-block;margin-top:18px;width:102px;height:32px;line-height:32px;font-size:15px}

/* services */
.service{position:absolute;left:157px;width:940px;height:140px}
.service .ring{position:absolute;left:0;top:0;width:98px;height:98px;border:4px solid var(--deep);border-radius:50%}
.service .ring svg{position:absolute;left:25px;top:25px}
.service h3{position:absolute;left:130px;top:-6px;font-size:27px;font-weight:400}
.service p{position:absolute;left:130px;top:36px;width:800px;font-size:14px;line-height:19px}
.read-more{position:absolute;left:130px;width:82px;height:26px;line-height:26px;font-size:14px;text-align:center;background:var(--accent-soft);color:var(--deep);border:1px solid var(--accent)}

/* footer */
.site-footer{position:absolute;top:3336px;left:0;width:1200px;height:227px;background:var(--deep);color:var(--white)}
.fcol{position:absolute;top:50px;font-size:12px;line-height:17px}
.fcol h4{font-size:13px;font-weight:400;letter-spacing:.5px;margin-bottom:8px}
.fcol li{list-style:none}
.email-field{width:156px;height:20px;background:var(--white);color:#666;font-size:11px;padding-left:4px;line-height:20px;margin-top:8px}
.subscribe{display:inline-block;margin-top:8px;padding:0 10px;height:22px;line-height:22px;background:var(--accent-soft);color:var(--deep);font-size:13px}
.footer-bar{position:absolute;top:3563px;left:0;width:1200px;height:39px;background:var(--deeper);color:var(--white)}
.footer-bar .copy{position:absolute;left:110px;top:13px;font-size:11px}
.footer-bar .mark{position:absolute;left:561px;top:6px;font-size:24px;letter-spacing:1px}
.social{position:absolute;left:910px;top:12px;display:flex;gap:12px}
.social i{width:14px;height:14px;border-radius:50%;background:var(--white)}
.to-top{position:absolute;left:1143px;top:3540px;width:34px;height:34px;background:var(--white)}
</style>
</head>
<body>

<header class="site-header">
  <div class="brand">Brovelle</div>
  <nav class="nav">
    <span class="current">Home</span><span>Features</span><span>Plans &amp; Pricing</span><span>Blog</span><span>Add-ons</span><span>Log in</span>
  </nav>
  <div class="btn-signup-sm">Sign up</div>
  <div class="lang"><i></i></div>
</header>

<section class="hero">
  <div class="hero-clouds" role="img" aria-label="Soft white cloud bank under a sunlit sky"></div>
  <h2 class="hero-title">SEO Tools you'll actually use</h2>
  <div class="feature" style="left:180px">
    <svg width="90" height="90" viewBox="0 0 90 90" fill="none" stroke="#1d2b30" stroke-width="5"><circle cx="50" cy="36" r="24"/><line x1="33" y1="53" x2="12" y2="76" stroke-width="8"/><polyline points="36,44 46,32 54,38 64,26" stroke-width="3"/></svg>
    <span>Track your Competition</span>
  </div>
  <div class="feature" style="left:465px">
    <svg width="90" height="90" viewBox="0 0 90 90" fill="none" stroke="#1d2b30" stroke-width="4"><circle cx="45" cy="45" r="36"/><polyline points="12,48 30,48 36,34 44,62 52,26 58,48 78,48"/></svg>
    <span>Analyze Results</span>
  </div>
  <div class="feature" style="left:720px">
    <svg width="90" height="90" viewBox="0 0 90 90" fill="none" stroke="#1d2b30" stroke-width="4"><rect x="14" y="16" width="62" height="50"/><line x1="4" y1="16" x2="86" y2="16"/><rect x="26" y="44" width="6" height="14" fill="#1d2b30"/><rect x="38" y="36" width="6" height="22" fill="#1d2b30"/><rect x="50" y="28" width="6" height="30" fill="#1d2b30"/><rect x="62" y="34" width="6" height="24" fill="#1d2b30"/></svg>
    <span>Improve Rankings</span>
  </div>
  <div class="btn-dark hero-cta">Sign up</div>
  <p class="hero-note">Lorem ipsum dolor sit amet, consectetur adipiscing elit</p>
</section>

<section class="intro">
  <h1>Lorem ipsum dolor sit amet</h1>
  <p class="lead">Consectetur adipiscing elit. Nulla lobortis consequat mauris, eget eleifend nunc viverra viverra.</p>
  <p class="accent">Ut ac risus odio. Aliquam pretium</p>
  <p class="small">purus sed nulla feugiat blandit. Cras vel libero ut lacus eleifend tempor. Phasellus eleifend,</p>
</section>

<div class="rule" style="top:857px"></div>

<section class="stats">
  <h2 class="abs stats-title" style="font-weight:400">Lorem ipsum dolor</h2>
  <p class="stats-sub">Consectetur adipiscing elit. Nulla lobortis consequat mauris, eget eleifend nunc viverra viverra. Ut ac</p>
  <div class="visit-bar">21,464 people visited this site</div>
  <svg class="abs" style="left:106px;top:1081px" width="180" height="180" viewBox="-90 -90 180 180">
    <path d="M0 0 L-89 -2 A89 89 0 1 0 69 -56 Z" fill="var(--blue)"/>
    <path d="M0 0 L69 -56 A89 89 0 0 0 25 -85 Z" fill="var(--orange)"/>
    <path d="M0 0 L25 -85 A89 89 0 0 0 -89 -2 Z" fill="var(--green)"/>
  </svg>
  <ul class="legend">
    <li><i style="background:var(--blue)"></i>61.99% Search Traffic<small>13,305 Visits</small></li>
    <li><i style="background:var(--green)"></i>25.16% Referral Traffic<small>5,401 Visits</small></li>
    <li><i style="background:var(--orange)"></i>12.49% Direct Traffic<small>2,681 Visits</small></li>
    <li><i style="background:var(--yellow)"></i>0.36% Campaigns<small>77 Visits</small></li>
  </ul>
  <div class="dashboard-shot" role="img" aria-label="Desktop monitor showing the analytics dashboard with traffic graph and source tables"></div>
</section>

<div class="rule" style="top:1389px"></div>

<h2 class="section-title" style="top:1434px;font-weight:400">Our Clients</h2>
<div class="clients">
  <span>Varnley</span><span>Orchida</span><span>Tallow</span><span>Brightpost</span><span>Kelva</span><span>Lumeo</span><span>Ombra</span><span>Pexio</span><span>Sundry</span>
</div>

<div class="rule" style="top:1587px"></div>

<section class="growth">
  <svg class="abs" style="left:110px;top:1660px" width="980" height="450" viewBox="110 1660 980 450">
    <g stroke="#eef2f3" stroke-width="1">
      <line x1="120" y1="1700" x2="1080" y2="1700"/><line x1="120" y1="1760" x2="1080" y2="1760"/><line x1="120" y1="1820" x2="1080" y2="1820"/><line x1="120" y1="1880" x2="1080" y2="1880"/><line x1="120" y1="1940" x2="1080" y2="1940"/><line x1="120" y1="2000" x2="1080" y2="2000"/><line x1="120" y1="2060" x2="1080" y2="2060"/>
    </g>
    <polyline fill="none" stroke="var(--line)" stroke-width="5" points="184,2084 260,1793 328,2011 399,1763 468,1758 539,1910 615,1993 686,1989 752,1954 825,1959 896,2040 997,1871 1043,1886"/>
    <g fill="var(--white)" stroke="var(--line)" stroke-width="4">
      <circle cx="184" cy="2084" r="9"/><circle cx="260" cy="1793" r="9"/><circle cx="328" cy="2011" r="9"/><circle cx="399" cy="1763" r="9"/><circle cx="468" cy="1758" r="9"/><circle cx="539" cy="1910" r="9"/><circle cx="615" cy="1993" r="9"/><circle cx="686" cy="1989" r="9"/><circle cx="752" cy="1954" r="9"/><circle cx="825" cy="1959" r="9"/><circle cx="896" cy="2040" r="9"/><circle cx="997" cy="1871" r="9"/><circle cx="1043" cy="1886" r="9"/>
    </g>
  </svg>
  <svg class="chart-icon" viewBox="0 0 64 54" fill="none" stroke="#1d2b30" stroke-width="4"><rect x="3" y="3" width="58" height="40"/><line x1="32" y1="43" x2="32" y2="52"/><line x1="20" y1="52" x2="44" y2="52"/><polyline points="12,34 24,22 32,28 48,12"/><polyline points="40,12 48,12 48,20"/></svg>
  <h3 class="chart-title" style="font-weight:400">Phasellus mollis pharetra dignissim</h3>
  <p class="chart-text">Ut pretium blandit lectus congue fringilla. Aliquam imperdiet ante quis odio congue ultrices. Donec at nisl augue, sit amet ultricies leo. Cras viverra lacinia magna, auctor convallis sapien interdum at</p>
  <div class="tooltip">Ut pretium blandit lectus congue fringilla. Aliquam imperdiet ante quis odio congue ultrices.</div>
</section>

<div class="rule" style="top:2172px"></div>

<section class="columns">
  <div class="col" style="left:124px">
    <h3>Mauris porta</h3>
    <div class="art" role="img" aria-label="Cluster of small green and blue app tiles" style="background:linear-gradient(135deg,#7cc453,#3fa4c8)"></div>
    <p>Ut pretium blandit lectus congue fringilla. Aliquam imperdiet ante quis odio congue ultrices. Donec at nisl augue,</p>
    <div class="btn-dark">Know More</div>
  </div>
  <div class="col" style="left:457px">
    <h3>Nulla lobortis</h3>
    <div class="art" role="img" aria-label="Magnifying glass over a bar chart sheet" style="background:linear-gradient(135deg,#e7eef0,#b9cfd6)"></div>
    <p>Ut pretium blandit lectus congue fringilla. Aliquam imperdiet ante quis odio congue ultrices. Donec at nisl augue,</p>
    <div class="btn-dark">Know More</div>
  </div>
  <div class="col" style="left:783px">
    <h3>Duis nec augue</h3>
    <div class="art" role="img" aria-label="Hand holding a banknote" style="background:linear-gradient(135deg,#58b9de,#2b8ab5)"></div>
    <p>Ut pretium blandit lectus congue fringilla. Aliquam imperdiet ante quis odio congue ultrices. Donec at nisl augue,</p>
    <div class="btn-dark">Know More</div>
  </div>
</section>

<div class="rule" style="top:2608px"></div>

<section class="services">
  <div class="service" style="top:2677px">
    <div class="ring"><svg width="40" height="40" viewBox="0 0 40 40" fill="#1d4a53"><circle cx="20" cy="15" r="12"/><rect x="14" y="26" width="12" height="10"/></svg></div>
    <h3>SEO Consultation Services</h3>
    <p>Consectetur adipiscing elit. Nulla lobortis consequat mauris, eget eleifend nunc viverra viverra. Ut ac risus odio. Aliquam pretium purus sed nulla feugiat blandit. Cras vel libero ut lacus eleifend tempor. Phasellus eleifend, magna</p>
    <div class="read-more" style="top:90px">Read More</div>
  </div>
  <div class="service" style="top:2841px">
    <div class="ring"><svg width="40" height="40" viewBox="0 0 40 40" fill="#1d4a53"><rect x="2" y="6" width="36" height="28" rx="3"/><circle cx="13" cy="17" r="5" fill="#fff"/><rect x="7" y="24" width="12" height="5" fill="#fff"/><rect x="23" y="14" width="11" height="3" fill="#fff"/><rect x="23" y="21" width="11" height="3" fill="#fff"/></svg></div>
    <h3>Social Profile Management</h3>
    <p>Consectetur adipiscing elit. Nulla lobortis consequat mauris, eget eleifend nunc viverra viverra. Ut ac risus odio. Aliquam pretium purus sed nulla feugiat blandit. Cras vel libero ut lacus eleifend tempor. Phasellus eleifend,</p>
    <div class="read-more" style="top:90px">Read More</div>
  </div>
  <div class="service" style="top:3002px">
    <div class="ring"><svg width="40" height="40" viewBox="0 0 40 40" fill="#1d4a53"><polygon points="14,2 26,2 23,9 17,9"/><polygon points="17,9 23,9 28,32 20,39 12,32"/></svg></div>
    <h3>Online Reputation Management</h3>
    <p>Consectetur adipiscing elit. Nulla lobortis consequat mauris, eget eleifend nunc viverra viverra. Ut ac risus odio. Aliquam pretium purus sed nulla feugiat blandit. Cras vel libero ut lacus eleifend tempor. Phasellus eleifend,</p>
    <div class="read-more" style="top:90px">Read More</div>
  </div>
  <div class="service" style="top:3167px">
    <div class="ring"><svg width="40" height="40" viewBox="0 0 40 40" fill="#1d4a53"><rect x="4" y="20" width="7" height="16"/><rect x="14" y="8" width="7" height="28"/><rect x="24" y="16" width="7" height="20"/><rect x="2" y="36" width="36" height="3"/></svg></div>
    <h3>Growth Hacking</h3>
    <p>Consectetur adipiscing elit. Nulla lobortis consequat mauris, eget eleifend nunc viverra viverra.</p>
    <div class="read-more" style="top:72px">Read More</div>
  </div>
</section>

<footer class="site-footer">
  <div class="fcol" style="left:110px"><h4>PRODUCTS</h4><ul><li>Home</li><li>Features</li><li>Plans &amp; Pricing</li><li>API</li><li>Case Studies</li><li>Affiliate Program</li></ul></div>
  <div class="fcol" style="left:240px"><h4>SUPPORT</h4><ul><li>Support &amp; FAQ</li><li>About Us</li><li>Jobs</li><li>SEO/SEM Knowledge Base</li></ul></div>
  <div class="fcol" style="left:426px"><h4>OTHER</h4><ul><li>Terms of Service</li><li>Use of cookies</li><li>Blog</li><li>Mobile</li><li>Startups</li></ul></div>
  <div class="fcol" style="left:561px"><h4>PRICING</h4><ul><li>Link Rates</li><li>Prepaid Packages</li></ul></div>
  <div class="fcol" style="left:700px;width:170px"><h4>NEWSLETTER</h4><p>Subscribe to our newsletter! Get productivity tips, product updates and special offers.</p><div class="email-field">Enter your email here</div><div class="subscribe">Subscribe</div></div>
  <div class="fcol" style="left:913px;width:180px"><h4>CONTACT US</h4><p>Iacus ut ullamcorper sodales, mauris tortor feugiat purus, nec aliquam</p><p style="margin-top:6px">UK: +0 (000) 000 0000<br>UK: +00 00 00 00 0000</p></div>
</footer>
<div class="footer-bar">
  <span class="copy">© All rights reserved 2013. Brovelle.</span>
  <span class="mark">Brovelle</span>
  <div class="social" aria-label="Social profiles"><i></i><i></i><i></i><i></i><i></i></div>
</div>
<div class="to-top"><svg width="34" height="34" viewBox="0 0 34 34"><polyline points="10,20 17,13 24,20" fill="none" stroke="#1d4a53" stroke-width="3"/></svg></div>

</body>
</html>
```